KestrelHollowCo.com

I need a site that I can sell dewatering equipment to the construction industry.
Ie, pipes fittings pumps and other such things needed to remove the groundwater on construction sites. Here in Florida, it’s needed almost everywhere seeing we are at sea level.
I want to be able to sell these products on the site and receive

```html
<!DOCTYPE html>
<html lang="en">
<head>
<meta charset="utf-8">
<title>KestrelHollowCo.com — Dewatering Equipment</title>
<link href="https://fonts.googleapis.com/css2?family=Oswald:wght@400;500;600&family=Raleway:wght@400;500;600&display=swap" rel="stylesheet">
<style>
:root{
  --teal:#0e9fb6;
  --teal-dark:#0b8396;
  --orange:#f4691c;
  --ink:#1e1e1e;
  --text:#444;
  --muted:#777;
  --rule:#dcdcdc;
  --footer:#06363f;
  --footer-deep:#042830;
  --white:#fff;
}
*{box-sizing:border-box;margin:0;padding:0}
html,body{width:1200px;height:2500px;overflow:hidden}
body{position:relative;font-family:"Raleway",Arial,sans-serif;color:var(--text);background:var(--white)}
.abs{position:absolute}
.heading{font-family:"Oswald",Arial,sans-serif;font-weight:500;letter-spacing:2px;text-transform:uppercase}

/* top bar */
.topbar{left:0;top:0;width:1200px;height:25px;background:var(--teal);color:var(--white);font-size:11px}
.topbar span{position:absolute;top:6px;display:flex;align-items:center;gap:5px}

/* header */
.header{left:0;top:25px;width:1200px;height:78px;background:var(--white)}
.brand{left:87px;top:12px}
.brand-name{font-family:"Oswald",Arial,sans-serif;font-weight:600;font-size:27px;color:var(--ink);line-height:1.1}
.brand-tag{font-size:13px;color:var(--teal);margin-top:1px}
.nav{top:38px;font-size:13px;color:var(--ink)}
.search{left:978px;top:36px;width:135px;height:22px;border-bottom:1px solid #bbb}

/* hero */
.hero{left:0;top:103px;width:1200px;height:530px;background:linear-gradient(110deg,#2a2a26 0%,#4a4a3c 25%,#6b5a2a 45%,#3f3d36 65%,#5a2e28 85%,#2d2c2a 100%)}
.hero-shade{left:0;top:0;width:1200px;height:530px;background:rgba(0,0,0,.35)}
.hero-title{left:0;top:158px;width:1200px;text-align:center;color:var(--white);font-size:58px;letter-spacing:2px}
.hero-copy{left:180px;top:246px;width:840px;text-align:center;color:var(--white);font-size:14px;line-height:23px}
.btn{display:flex;align-items:center;justify-content:center;background:var(--orange);color:var(--white);font-family:"Oswald",Arial,sans-serif;border-radius:30px;letter-spacing:1px}
.hero-btn{left:526px;top:325px;width:148px;height:50px;font-size:15px}
.arrow{color:var(--white)}

/* welcome */
.section-title{left:0;width:1200px;text-align:center;color:var(--teal);font-size:31px}
.underline{height:2px;width:52px;left:574px}
.welcome-copy{left:160px;top:752px;width:880px;text-align:center;font-size:13.5px;line-height:22px;color:var(--text)}
.service-img{top:897px;width:325px;height:233px}
.service-name{top:1152px;width:325px;text-align:center;color:var(--teal);font-family:"Oswald",Arial,sans-serif;font-size:21px;text-transform:uppercase}

/* products */
.products{left:0;top:1237px;width:1200px;height:401px;background:linear-gradient(180deg,#151515,#1f1f1f 50%,#141414)}
.product-card{top:115px;width:237px;height:231px;background:var(--white)}
.product-card .photo{width:237px;height:190px}
.product-card .label{position:absolute;left:0;bottom:0;width:237px;height:41px;background:var(--teal);color:var(--white);display:flex;align-items:center;justify-content:center;font-family:"Oswald",Arial,sans-serif;font-size:16px;letter-spacing:.5px}
.product-card.featured{background:var(--teal);color:var(--white);text-align:center}

/* news */
.news-title{font-family:"Oswald",Arial,sans-serif;font-size:18px;color:var(--ink);line-height:1.2}
.news-meta{font-size:12px;color:var(--orange)}
.news-meta .sep{color:#999;margin:0 6px}
.news-body{font-size:12.5px;line-height:21px;color:var(--text)}
.read-more{font-size:12px;color:var(--orange)}
.news-rule{height:1px;background:var(--rule);width:500px}
.news-thumb{width:112px;height:130px}

/* footer */
.footer{left:0;top:2275px;width:1200px;height:188px;background:var(--footer);color:var(--white)}
.footer .brand-name{color:var(--white)}
.copyright{left:0;top:2463px;width:1200px;height:37px;background:var(--footer-deep);color:var(--white);font-size:12px}
</style>
</head>
<body>

<!-- top bar -->
<div class="abs topbar">
  <span style="left:625px">Have any questions? Contact us</span>
  <span style="left:830px">
    <svg width="11" height="9" viewBox="0 0 11 9"><rect x="0.5" y="0.5" width="10" height="8" fill="none" stroke="#fff"/><path d="M0.5 0.5 L5.5 5 L10.5 0.5" fill="none" stroke="#fff"/></svg>
    sales@companyname.com</span>
  <span style="left:1018px">
    <svg width="10" height="10" viewBox="0 0 24 24"><path fill="#fff" d="M6.6 10.8a15.1 15.1 0 0 0 6.6 6.6l2.2-2.2a1 1 0 0 1 1-.25 11.4 11.4 0 0 0 3.6.57 1 1 0 0 1 1 1V20a1 1 0 0 1-1 1A17 17 0 0 1 3 4a1 1 0 0 1 1-1h3.5a1 1 0 0 1 1 1c0 1.25.2 2.45.57 3.57a1 1 0 0 1-.25 1z"/></svg>
    0987 - 654 - 321</span>
</div>

<!-- header -->
<header class="abs header">
  <div class="abs brand">
    <div class="brand-name">KestrelHollowCo.com</div>
    <div class="brand-tag">Sed ut perspiciatis unde omnis</div>
  </div>
  <nav>
    <span class="abs nav" style="left:511px">Home</span>
    <span class="abs nav" style="left:589px">About Us</span>
    <span class="abs nav" style="left:688px">Products</span>
    <span class="abs nav" style="left:785px">News</span>
    <span class="abs nav" style="left:861px">Contact us</span>
  </nav>
  <div class="abs search">
    <svg class="abs" style="left:2px;top:3px" width="13" height="13" viewBox="0 0 13 13"><circle cx="5.5" cy="5.5" r="4" fill="none" stroke="#222" stroke-width="2"/><line x1="8.5" y1="8.5" x2="12" y2="12" stroke="#222" stroke-width="2"/></svg>
  </div>
</header>

<!-- hero -->
<section class="abs hero" role="img" aria-label="Close-up photograph of a yellow industrial dewatering pump with red motor housing">
  <div class="abs hero-shade"></div>
  <h1 class="abs heading hero-title">Dewatering Pumps</h1>
  <p class="abs hero-copy">Sed ut perspiciatis unde omnis iste natus error sit voluptatem accusantium doloremque laudantium, totam rem aperiam, eaque ipsa quae ab illo inventore veritatis et quasi architecto beatae vitae</p>
  <div class="abs btn hero-btn">LEARN MORE</div>
  <svg class="abs arrow" style="left:20px;top:245px" width="20" height="34" viewBox="0 0 20 34"><path d="M16 3 L4 17 L16 31" fill="none" stroke="#fff" stroke-opacity=".75" stroke-width="4"/></svg>
  <svg class="abs arrow" style="left:1160px;top:245px" width="20" height="34" viewBox="0 0 20 34"><path d="M4 3 L16 17 L4 31" fill="none" stroke="#fff" stroke-opacity=".75" stroke-width="4"/></svg>
</section>

<!-- welcome -->
<section>
  <h2 class="abs heading section-title" style="top:682px">Welcome to our website</h2>
  <div class="abs underline" style="top:735px;background:#777"></div>
  <p class="abs welcome-copy">Sed ut perspiciatis unde omnis iste natus error sit voluptatem accusantium doloremque laudantium, totam rem aperiam, eaque ipsa quae ab illo inventore veritatis et quasi architecto beatae vitae dicta sunt explicabo. Nemo enim ipsam voluptatem quia voluptas sit aspernatur aut odit aut fugit, sed quia consequuntur magni dolores eos qui ratione voluptatem sequi nesciunt. Neque porro quisquam est, qui dolorem ipsum quia dolor sit amet, consectetur, adipisci velit, sed quia non</p>

  <div class="abs service-img" style="left:87px;background:linear-gradient(180deg,#8fa0ac 0%,#6f6152 40%,#5b4a3a 70%,#3f64c4 100%)" role="img" aria-label="Blue dewatering pump beside an excavated trench on a construction site"></div>
  <div class="abs service-name" style="left:87px">Construction Dewatering</div>

  <div class="abs service-img" style="left:438px;background:linear-gradient(160deg,#7a5a3a 0%,#c07a30 30%,#3a3f9e 60%,#b8b6b0 100%)" role="img" aria-label="Row of blue electric pumps in an industrial plant room"></div>
  <div class="abs service-name" style="left:438px">Pumps and Equipment Rental</div>

  <div class="abs service-img" style="left:788px;background:linear-gradient(180deg,#6e8a5a 0%,#d4532a 40%,#c24a26 60%,#333 85%,#8a8a86 100%)" role="img" aria-label="Orange trailer-mounted bypass pumps with black suction hoses"></div>
  <div class="abs service-name" style="left:788px">Bypass Pumping</div>
</section>

<!-- products -->
<section class="abs products" role="region" aria-label="Our product">
  <h2 class="abs heading section-title" style="top:28px;color:var(--white)">Our Product</h2>
  <div class="abs underline" style="top:78px;background:var(--teal)"></div>

  <svg class="abs" style="left:48px;top:225px" width="18" height="26" viewBox="0 0 18 26"><path d="M14 3 L4 13 L14 23" fill="none" stroke="#fff" stroke-width="4"/></svg>
  <svg class="abs" style="left:1134px;top:225px" width="18" height="26" viewBox="0 0 18 26"><path d="M4 3 L14 13 L4 23" fill="none" stroke="#fff" stroke-width="4"/></svg>

  <div class="abs product-card featured" style="left:87px">
    <div class="abs" style="left:0;top:70px;width:237px;font-family:'Oswald',Arial,sans-serif;font-size:19px">DEWATERING PUMP</div>
    <div class="abs" style="left:0;top:103px;width:237px;font-size:13px">Diesel driven dewatering pump</div>
    <div class="abs btn" style="left:65px;top:132px;width:108px;height:40px;font-size:12px;font-family:'Raleway',Arial,sans-serif;letter-spacing:0">VIEW DETAILS</div>
  </div>

  <div class="abs product-card" style="left:350px">
    <div class="photo" style="background:radial-gradient(ellipse 45% 35% at 50% 52%,#2d8a5a 0%,#3b6c8a 55%,#fff 100%)" role="img" aria-label="Green and blue centrifugal slurry pump on a base frame"></div>
    <div class="label">DEWATERING PUMP</div>
  </div>
  <div class="abs product-card" style="left:613px">
    <div class="photo" style="background:radial-gradient(ellipse 32% 40% at 50% 50%,#2b4f7a 0%,#5e7a98 55%,#fff 100%)" role="img" aria-label="Compact blue electric centrifugal pump"></div>
    <div class="label">DEWATERING PUMP</div>
  </div>
  <div class="abs product-card" style="left:876px">
    <div class="photo" style="background:radial-gradient(ellipse 45% 30% at 50% 52%,#2f63b8 0%,#7f9cc8 55%,#fff 100%)" role="img" aria-label="Blue end-suction pump with motor on a skid"></div>
    <div class="label">DEWATERING PUMP</div>
  </div>
</section>

<!-- news -->
<section>
  <h2 class="abs heading section-title" style="top:1690px">Latest News</h2>
  <div class="abs underline" style="top:1740px;background:#777"></div>

  <!-- left column -->
  <article>
    <div class="abs news-title" style="left:87px;top:1773px">Vero eos et accusamus et iusto odio dignissimos ducimus</div>
    <div class="abs news-meta" style="left:87px;top:1808px">in Feb 11, 2018<span class="sep">|</span>by Admin</div>
    <p class="abs news-body" style="left:87px;top:1835px;width:500px">Lorem ipsum dolor sit amet, consectetur adipiscing elit, sed do eiusmod tempor incididunt ut labore et dolore magna aliqua...</p>
    <div class="abs read-more" style="left:87px;top:1894px">Read More »</div>
    <div class="abs news-rule" style="left:87px;top:1940px"></div>
  </article>
  <article>
    <div class="abs news-title" style="left:87px;top:1971px">Vero eos et accusamus et iusto odio dignissimos ducimus</div>
    <div class="abs news-meta" style="left:87px;top:2006px">in Feb 11, 2018<span class="sep">|</span>by Admin</div>
    <p class="abs news-body" style="left:87px;top:2033px;width:500px">Lorem ipsum dolor sit amet, consectetur adipiscing elit, sed do eiusmod tempor incididunt ut labore et dolore magna aliqua...</p>
    <div class="abs read-more" style="left:87px;top:2092px">Read More »</div>
    <div class="abs news-rule" style="left:87px;top:2138px"></div>
  </article>

  <!-- right column -->
  <article>
    <div class="abs news-thumb" style="left:613px;top:1777px;background:linear-gradient(160deg,#9aa3a6,#3a3a3a 55%,#7a7670)" role="img" aria-label="Portable petrol water pumps on a workshop floor"></div>
    <div class="abs news-title" style="left:743px;top:1773px">Vero eos et accusamus et iusto odio dignissimos</div>
    <div class="abs news-meta" style="left:743px;top:1808px">in Feb 11, 2018<span class="sep">|</span>by Admin</div>
    <p class="abs news-body" style="left:743px;top:1835px;width:370px">Lorem ipsum dolor sit amet, consectetur adipiscing elit, sed do eiusmod tempor incididunt ut ...</p>
    <div class="abs read-more" style="left:743px;top:1894px">Read More »</div>
    <div class="abs news-rule" style="left:613px;top:1940px"></div>
  </article>
  <article>
    <div class="abs news-thumb" style="left:613px;top:1975px;background:linear-gradient(160deg,#8a8f96,#2e4f9e 50%,#3f8a4a 80%,#b5b5b0)" role="img" aria-label="Blue pumps and green pipework in a plant room"></div>
    <div class="abs news-title" style="left:743px;top:1971px">Vero eos et accusamus et iusto odio dignissimos</div>
    <div class="abs news-meta" style="left:743px;top:2006px">in Feb 11, 2018<span class="sep">|</span>by Admin</div>
    <p class="abs news-body" style="left:743px;top:2033px;width:370px">Lorem ipsum dolor sit amet, consectetur adipiscing elit, sed do eiusmod tempor incididunt ut ...</p>
    <div class="abs read-more" style="left:743px;top:2092px">Read More »</div>
    <div class="abs news-rule" style="left:613px;top:2138px"></div>
  </article>

  <div class="abs btn" style="left:547px;top:2175px;width:106px;height:40px;font-size:14px;letter-spacing:0">VIEW ALL</div>
</section>

<!-- footer -->
<footer class="abs footer">
  <div class="abs" style="left:87px;top:30px">
    <div class="brand-name" style="font-size:26px">KestrelHollowCo.com</div>
    <div class="brand-tag">Sed ut perspiciatis unde omnis</div>
  </div>
  <p class="abs" style="left:87px;top:96px;width:740px;font-size:13px;line-height:22px">Sed ut perspiciatis unde omnis iste natus error sit voluptatem accusantium doloremque laudantium, totam rem aperiam, eaque ipsa quae ab illo inventore veritatis et quasi architecto beatae vitae dicta sunt explicabo.</p>
  <div class="abs" style="left:87px;top:153px;display:flex;gap:18px">
    <span style="width:20px;height:20px;border-radius:3px;background:var(--white)"></span>
    <span style="width:20px;height:20px;border-radius:3px;background:var(--white)"></span>
    <span style="width:20px;height:20px;border-radius:3px;background:var(--white)"></span>
  </div>

  <div class="abs" style="left:875px;top:29px;font-family:'Oswald',Arial,sans-serif;font-size:20px">CONTACT DETAILS</div>
  <svg class="abs" style="left:878px;top:82px" width="12" height="16" viewBox="0 0 12 16"><path fill="#fff" d="M6 0a6 6 0 0 0-6 6c0 4.5 6 10 6 10s6-5.5 6-10a6 6 0 0 0-6-6zm0 8.5A2.5 2.5 0 1 1 6 3.5a2.5 2.5 0 0 1 0 5z"/></svg>
  <div class="abs" style="left:898px;top:80px;font-size:13px;line-height:19px">ipsa quae 1445 Marlow Avenue<br>Suite 5454, iste natus Texas 75202</div>
  <svg class="abs" style="left:878px;top:135px" width="14" height="13" viewBox="0 0 14 13"><rect x="1" y="4" width="12" height="8" rx="1" fill="#fff"/><rect x="3" y="0.5" width="8" height="4" fill="none" stroke="#fff"/></svg>
  <div class="abs" style="left:898px;top:133px;font-size:13px">214.555.0610</div>
  <svg class="abs" style="left:1003px;top:134px" width="13" height="13" viewBox="0 0 24 24"><path fill="#fff" d="M6.6 10.8a15.1 15.1 0 0 0 6.6 6.6l2.2-2.2a1 1 0 0 1 1-.25 11.4 11.4 0 0 0 3.6.57 1 1 0 0 1 1 1V20a1 1 0 0 1-1 1A17 17 0 0 1 3 4a1 1 0 0 1 1-1h3.5a1 1 0 0 1 1 1c0 1.25.2 2.45.57 3.57a1 1 0 0 1-.25 1z"/></svg>
  <div class="abs" style="left:1026px;top:133px;font-size:13px">214.555.6103</div>
</footer>

<div class="abs copyright"><span class="abs" style="left:87px;top:11px">© Copyright 2018.All rights reserved. <span style="color:var(--teal)">Privacy Policy</span></span></div>

</body>
</html>
```